Modern Banner for use on Emails and Electronic letters.

We need a Email banner that we can also uses as a banner on electronic documents . Would be a bonus to be able to use banner on pixmingle.
The banner should incorporate our logo and company name; The ProVela Group.
We would like an eye catching, modern design.
We are completely open to using colour and/or images along with our logo and company name.
Currently the font for our company name is time new roman but again we are open to suggestions. The company name can be be moved away from the umbrella logo to anywhere in the banner.

Industry/Entity Type

Electronic

Font styles to use
Serif
Sans Serif

Colors

Designer to choose colors to be used in the design.

Requirements
Must have
• ProVela Logo (Umbrella design - Black umbrella on red blocks with a letter on each block spelling VELA.
• Company name: The ProVela Group
• Be Modern and professional.
• Suitable for use as an email banner but can also be used as letterhead on electronic documents.
Nice to have
• Colour and/or images.
• Be able to be used as pixmingle banner.

```html
<!DOCTYPE html>
<html lang="en">
<head>
<meta charset="utf-8">
<title>The ProVela Group — Letterhead</title>
<link href="https://fonts.googleapis.com/css2?family=Tinos&family=Open+Sans:wght@400;600&display=swap" rel="stylesheet">
<style>
  :root {
    --backdrop: #f7c9c6;
    --paper: #ffffff;
    --brand-red: #d7263d;
    --ink: #1d1d1d;
    --steel: #5a5a5a;
    --leaf: #8cc63f;
    --leaf-light: #c9e48f;
    --watermark: #efefef;
  }
  * { box-sizing: border-box; margin: 0; padding: 0; }
  html, body { width: 1200px; height: 784px; overflow: hidden; }
  body { background: var(--backdrop); position: relative; }

  .letterhead {
    position: absolute; left: 337px; top: 20px;
    width: 526px; height: 744px;
    background: var(--paper);
    box-shadow: 0 6px 24px rgba(150, 60, 60, 0.18);
    overflow: hidden;
  }

  .corner-marks { position: absolute; top: 0; display: flex; gap: 4px; }
  .corner-marks--left { left: 30px; }
  .corner-marks--right { right: 30px; }
  .corner-marks span { display: block; width: 24px; height: 5px; }
  .corner-marks .mark-red { background: var(--brand-red); }
  .corner-marks .mark-grey { background: var(--steel); }

  .brand {
    position: absolute; left: 34px; top: 28px;
    display: flex; align-items: center; gap: 8px;
  }
  .brand-square { width: 14px; height: 14px; background: var(--brand-red); }
  .brand-name {
    font-family: "Tinos", "Times New Roman", serif;
    font-size: 19px; color: var(--ink); letter-spacing: 0.2px;
  }

  .contact {
    position: absolute; right: 30px; top: 30px;
    font-family: "Open Sans", Arial, sans-serif;
    font-size: 7.5px; line-height: 1.55; color: var(--steel);
    list-style: none;
  }
  .contact li { display: flex; align-items: center; gap: 5px; white-space: nowrap; }
  .contact li::before {
    content: ""; width: 5px; height: 5px; border-radius: 50%;
    background: var(--brand-red); flex: none;
  }

  .watermark {
    position: absolute; left: 40px; top: 300px;
    width: 230px; height: 230px; border-radius: 50%;
    background: radial-gradient(circle at 50% 45%, var(--watermark), rgba(239,239,239,0) 70%);
  }

  .footer-bands { position: absolute; left: 0; bottom: 0; width: 100%; height: 60px; }

  .partner-badge {
    position: absolute; left: 352px; top: 660px;
    width: 130px; height: 34px; border-radius: 6px;
    background: var(--leaf); opacity: 0.55;
  }
</style>
</head>
<body>
  <main class="letterhead">
    <div class="corner-marks corner-marks--left"><span class="mark-red"></span><span class="mark-grey"></span></div>
    <div class="corner-marks corner-marks--right"><span class="mark-red"></span><span class="mark-grey"></span></div>

    <header class="brand">
      <span class="brand-square"></span>
      <span class="brand-name">The ProVela Group</span>
    </header>

    <ul class="contact">
      <li>120 Harbor Lane, Suite 400,</li>
      <li>Riverton, TX 75001</li>
      <li>(555) 014-2280</li>
      <li>(555) 014-3391</li>
      <li>info@provela.com</li>
      <li>www.provela.com</li>
    </ul>

    <div class="watermark" role="img" aria-label="Faint brand decoration area"></div>

    <svg class="footer-bands" viewBox="0 0 526 60" preserveAspectRatio="none" aria-hidden="true">
      <defs>
        <linearGradient id="leafFade" x1="0" x2="1" y1="0" y2="0">
          <stop offset="0" stop-color="#8cc63f"/>
          <stop offset="1" stop-color="#c9e48f" stop-opacity="0.15"/>
        </linearGradient>
      </defs>
      <line x1="0" y1="24" x2="150" y2="24" stroke="#5a5a5a" stroke-width="2"/>
      <line x1="160" y1="24" x2="330" y2="24" stroke="#8cc63f" stroke-width="2"/>
      <polygon points="0,32 330,32 318,44 0,44" fill="#d7263d"/>
      <polygon points="336,32 526,32 526,60 314,60" fill="url(#leafFade)"/>
      <polygon points="0,44 318,44 304,60 0,60" fill="#ffffff"/>
    </svg>

    <div class="partner-badge" role="img" aria-label="Partner badge"></div>
  </main>
</body>
</html>
```